Book cover design for modern bagpipe music book

This music book will be A4 in size and requires a design for the front and back cover. The focus is on creating a modern and eye catching design, breaking away from the stereotypes of what people think of when they think of bagpipes. Think the OPPOSITE of a bagpiper in a full kilt standing on top of a mountain playing Lanterns on the Moor!

Book title: Wake Stroll Hum Again

Other front cover text : Music for the bagpipes by Dara Colby

Front cover file ideas uploaded

2 pictures of bagpipes attached.

- The real set of bagpipes give an idea of the correct finer details

- The toy bagpipes perhaps have a better shape with the left 'stick' down

Back cover - No real brief. Keen for it not to be a full block single colour though.

Design requires 3mm bleed for print

Open to ideas and suggestions! Thank you!

```html
<!DOCTYPE html>
<html lang="en">
<head>
<meta charset="utf-8">
<title>Wake Stroll Hum Again – Music for the Bagpipes</title>
<link rel="stylesheet" href="https://fonts.googleapis.com/css2?family=League+Gothic&family=Montserrat:wght@800;900&display=swap">
<style>
  :root {
    --page: #ecebe7;
    --cover: #1d1d1e;
    --cover-edge: #141415;
    --white: #f4f4f2;
    --gold-light: #f3e3a6;
    --gold-mid: #d3b66a;
    --gold-dark: #a88636;
    --tartan-red: #c8161d;
    --tartan-deep: #8e0d14;
  }
  * { box-sizing: border-box; margin: 0; padding: 0; }
  html, body { width: 1200px; height: 674px; overflow: hidden; background: var(--page); }
  .spread { position: relative; width: 1200px; height: 674px; }

  .cover {
    position: absolute; top: 93px; width: 342px; height: 479px;
    background: linear-gradient(135deg, #262627 0%, var(--cover) 55%, var(--cover-edge) 100%);
    color: var(--white);
    overflow: hidden;
  }
  .cover--back { left: 207px; }
  .cover--front { left: 648px; }

  /* Back cover */
  .icon-stack {
    position: absolute; top: 50px; left: 50%; transform: translateX(-50%);
    display: flex; flex-direction: column; gap: 18px;
  }
  .icon-tile { width: 75px; height: 75px; display: block; }

  .credit {
    position: absolute; left: 0; right: 0; text-align: center;
    font-family: "Montserrat", sans-serif; font-weight: 800;
    letter-spacing: 0.02em; text-transform: uppercase;
  }
  .credit--subtitle { top: 430px; font-size: 11px; }
  .credit--author { top: 446px; font-size: 19px; font-weight: 900; }

  /* Front cover */
  .title {
    position: absolute; left: 27px; top: 22px;
    font-family: "League Gothic", sans-serif; font-weight: 400;
    text-transform: uppercase; line-height: 1;
  }
  .title__word { display: block; font-size: 68px; transform: scaleX(0.82); transform-origin: left; }
  .title__word--wake { margin-bottom: 10px; }
  .title__word--hum {
    font-size: 182px; line-height: 0.78; margin: 16px 0 20px; letter-spacing: -0.01em;
    background: linear-gradient(160deg, var(--tartan-red) 0%, #d9242a 45%, var(--tartan-deep) 100%);
    -webkit-background-clip: text; background-clip: text; color: transparent;
  }

  .front-subtitle {
    position: absolute; left: 60px; top: 436px;
    font-family: "Montserrat", sans-serif; font-weight: 800; font-size: 12.5px;
    text-transform: uppercase; letter-spacing: 0.02em;
  }

  .front-author {
    position: absolute; left: 272px; top: 402px;
    width: 396px; height: 46px;
    transform: rotate(-90deg); transform-origin: left top;
    white-space: nowrap;
    font-family: "Montserrat", sans-serif; font-weight: 900; font-size: 33px;
    line-height: 46px; letter-spacing: 0.14em; text-transform: uppercase;
    background: linear-gradient(90deg, var(--gold-dark) 0%, var(--gold-light) 45%, var(--gold-mid) 100%);
    -webkit-background-clip: text; background-clip: text; color: transparent;
  }
</style>
</head>
<body>
<main class="spread">

  <section class="cover cover--back" aria-label="Back cover">
    <svg width="0" height="0" style="position:absolute" aria-hidden="true">
      <defs>
        <linearGradient id="gold" x1="0" y1="0" x2="1" y2="1">
          <stop offset="0" stop-color="#f3e3a6"/>
          <stop offset="0.5" stop-color="#d3b66a"/>
          <stop offset="1" stop-color="#a88636"/>
        </linearGradient>
      </defs>
    </svg>

    <div class="icon-stack">
      <!-- Wake: rising sun -->
      <svg class="icon-tile" viewBox="0 0 75 75" aria-label="Wake icon" role="img">
        <rect x="3" y="3" width="69" height="69" rx="9" fill="none" stroke="url(#gold)" stroke-width="3.5"/>
        <path d="M22 48a15.5 15.5 0 0 1 31 0z" fill="url(#gold)"/>
        <rect x="16" y="51" width="43" height="4" rx="2" fill="url(#gold)"/>
        <g stroke="url(#gold)" stroke-width="3.5" stroke-linecap="round">
          <line x1="37.5" y1="17" x2="37.5" y2="25"/>
          <line x1="20" y1="25" x2="25" y2="30"/>
          <line x1="55" y1="25" x2="50" y2="30"/>
        </g>
      </svg>
      <!-- Stroll: winding path arrow -->
      <svg class="icon-tile" viewBox="0 0 75 75" aria-label="Stroll icon" role="img">
        <rect x="3" y="3" width="69" height="69" rx="9" fill="none" stroke="url(#gold)" stroke-width="3.5"/>
        <path d="M18 56c10 0 12-12 20-12s10-12 18-18" fill="none" stroke="url(#gold)" stroke-width="4.5" stroke-linecap="round"/>
        <path d="M46 22l12 2-3 12z" fill="url(#gold)"/>
      </svg>
      <!-- Hum: music note -->
      <svg class="icon-tile" viewBox="0 0 75 75" aria-label="Hum icon" role="img">
        <rect x="3" y="3" width="69" height="69" rx="9" fill="none" stroke="url(#gold)" stroke-width="3.5"/>
        <path d="M31 50V22l20-5v27" fill="none" stroke="url(#gold)" stroke-width="4"/>
        <ellipse cx="26" cy="51" rx="7" ry="5.5" fill="url(#gold)"/>
        <ellipse cx="46" cy="45" rx="7" ry="5.5" fill="url(#gold)"/>
      </svg>
      <!-- Again: repeat arrow -->
      <svg class="icon-tile" viewBox="0 0 75 75" aria-label="Again icon" role="img">
        <rect x="3" y="3" width="69" height="69" rx="9" fill="none" stroke="url(#gold)" stroke-width="3.5"/>
        <path d="M51 30a15 15 0 1 0 2 12" fill="none" stroke="url(#gold)" stroke-width="6" stroke-linecap="round"/>
        <path d="M43 20l14 2-4 13z" fill="url(#gold)"/>
      </svg>
    </div>

    <p class="credit credit--subtitle">Music for the bagpipes</p>
    <p class="credit credit--author">By Dara Colby</p>
  </section>

  <section class="cover cover--front" aria-label="Front cover">
    <h1 class="title">
      <span class="title__word title__word--wake">Wake</span>
      <span class="title__word title__word--stroll">Stroll</span>
      <span class="title__word title__word--hum" role="img" aria-label="Tartan-filled lettering: HUM">Hum</span>
      <span class="title__word title__word--again">Again</span>
    </h1>
    <p class="front-subtitle">Music for the bagpipes</p>
    <p class="front-author">By Dara Colby</p>
  </section>

</main>
</body>
</html>
```